Website for new dental office

I am Dr. Colin Marsh and am building a new dental practice. I specialize in general dentistry. I am young and have a higher end dental practice incorporating very new technologies and would like my website to reflect that. As many dental patients are older, the website must be very easy to navigate. I would like patients to be able to request appointments, and will eventually add on patient information forms (the health history, etc, that you normally fill out in the practice) from my practice management software, so leave an area for that.

Industry/Entity Type

Building

```html
<!DOCTYPE html>
<html lang="en">
<head>
<meta charset="utf-8">
<title>Marsh Dental</title>
<link href="https://fonts.googleapis.com/css2?family=Open+Sans:wght@300;400;600;700&family=Caveat:wght@600&display=swap" rel="stylesheet">
<style>
:root{
  --blue:#0a7fcf;
  --blue-dark:#0660a8;
  --navy:#0b4fa3;
  --text:#666;
  --text-dark:#333;
  --muted:#999;
  --light:#e8f3fa;
  --line:#d8e6ef;
  --white:#fff;
}
*{margin:0;padding:0;box-sizing:border-box}
html,body{width:835px;height:1200px;overflow:hidden;background:var(--white)}
body{font-family:"Open Sans",sans-serif;color:var(--text);position:relative}
svg{display:block}

/* header */
.site-header{position:absolute;left:0;top:0;width:835px;height:82px;background:var(--white);box-shadow:0 2px 6px rgba(0,0,0,.06);z-index:3}
.brand{position:absolute;left:77px;top:14px;color:var(--navy);font-weight:600;line-height:1;letter-spacing:-.5px}
.brand .b1{font-size:30px;display:block}
.brand .b2{font-size:21px;display:block;margin-top:3px}
.main-nav{position:absolute;left:236px;top:0;display:flex;height:82px}
.nav-item{height:82px;display:flex;flex-direction:column;align-items:center;justify-content:center;font-size:11px;color:#8a8a8a;padding:0 13px}
.nav-item svg{margin-bottom:8px}
.nav-item.active{background:var(--blue);color:var(--white);width:65px;padding:0}
.header-contact{position:absolute;left:698px;top:17px;font-size:8.5px;color:var(--muted);line-height:14px}
.header-contact .phone{color:var(--blue);font-size:11px;font-weight:600}
.header-contact .row{display:flex;gap:10px}

/* hero */
.hero{position:absolute;left:0;top:82px;width:835px;height:315px;background:linear-gradient(90deg,#cfe6f5 0%,#e3f1fa 50%,#f2f8fc 100%);overflow:hidden}
.hero-photo{position:absolute;left:0;top:0;width:470px;height:315px;background:linear-gradient(90deg,#9cc9e8 0%,#c8dfee 45%,#e0eef7 100%)}
.hero-title{position:absolute;left:470px;top:56px;width:340px;font-family:"Caveat",cursive;font-size:27px;line-height:1.1;color:var(--navy);white-space:nowrap}
.hero-sub{position:absolute;left:470px;top:102px;font-size:15px;font-weight:300;color:#777;line-height:23px}
.btn-solid{position:absolute;background:var(--blue);color:var(--white);font-weight:600;display:flex;align-items:center;justify-content:center}
.hero-btn{left:470px;top:169px;width:107px;height:34px;font-size:10px;border:1px solid var(--navy)}

/* info cards */
.info-card{position:absolute;top:338px;width:189px;height:142px;background:var(--blue);color:var(--white);padding:14px 18px}
.info-card h3{font-weight:400;font-size:16px;margin-bottom:12px}
.info-card p{font-size:8px;line-height:13px}
.info-card .fold{position:absolute;right:0;bottom:0;width:0;height:0;border-left:19px solid #b7d3e8;border-top:19px solid transparent}
.info-card .fold::after{content:"";position:absolute;left:-19px;top:-19px;border-right:19px solid var(--blue-dark);border-top:19px solid transparent}
.btn-outline{position:absolute;left:18px;top:100px;width:63px;height:21px;border:1px solid var(--white);font-size:8px;display:flex;align-items:center;justify-content:center}
.btn-outline.filled{background:var(--white);color:var(--text-dark)}
.schedule-row{display:flex;justify-content:space-between;font-size:8px;padding:9px 0;border-bottom:1px solid rgba(255,255,255,.25)}
.schedule-row:last-child{border:none}

/* intro */
.section-title{position:absolute;font-weight:300;color:#444}
.intro-photo{position:absolute;left:36px;top:548px;width:177px;height:223px;background:linear-gradient(135deg,#f3ede8,#e9d6ca 55%,#dfe9ef)}
.intro-text{position:absolute;left:232px;top:546px;width:340px;font-size:8px;line-height:14px;color:#777}
.intro-strong{position:absolute;left:231px;top:590px;font-size:9.5px;font-weight:600;color:var(--text-dark)}
.treatments{position:absolute;left:231px;top:619px;display:grid;grid-template-columns:195px 170px;row-gap:9px}
.treatment{display:flex;align-items:center;gap:6px;font-size:8px;color:#888;height:18px}

/* booking */
.booking{position:absolute;left:609px;top:510px;width:191px;height:263px;background:var(--light);border:1px solid var(--line)}
.booking-head{height:29px;background:var(--blue);color:var(--white);font-size:9.5px;font-weight:600;display:flex;align-items:center;gap:7px;padding-left:17px;position:relative}
.booking-head .fold{position:absolute;right:-1px;bottom:-1px;border-left:10px solid transparent;border-bottom:10px solid var(--light)}
.field{position:absolute;left:17px;width:156px;height:22px;background:var(--white);border:1px solid var(--line);font-size:8px;color:#888;padding:0 7px;display:flex;align-items:center}
.field.typed{color:var(--text-dark)}
.field .caret{position:absolute;right:0;top:0;width:22px;height:20px;border-left:1px solid var(--line);display:flex;align-items:center;justify-content:center}
.submit{left:60px;top:224px;width:70px;height:21px;font-size:8.5px;font-weight:400;border:1px solid var(--navy)}

/* team */
.member{position:absolute;top:805px;width:171px;height:214px;border:1px solid #e2e2e2;background:var(--white)}
.member-photo{height:122px;background:linear-gradient(180deg,#e6e7e9,#d9dbde)}
.member h4{color:var(--blue);font-size:10px;font-weight:600;margin:14px 0 4px 12px}
.member p{font-size:8px;line-height:14.5px;color:#999;margin:0 12px}
.team-text{position:absolute;left:606px;top:838px;width:170px;font-size:8px;line-height:13px;color:#888}
.team-btn{left:607px;top:905px;width:69px;height:22px;font-size:8.5px;font-weight:400}
.arrow-btn{position:absolute;top:945px;width:19px;height:19px;border-radius:50%;display:flex;align-items:center;justify-content:center;border:1px solid var(--blue)}

/* footer */
.footer-brand{position:absolute;left:39px;top:1058px;color:var(--navy);font-weight:600;line-height:1}
.footer-brand .b1{font-size:30px;display:block}
.footer-brand .b2{font-size:20px;display:block;margin-top:3px}
.footer-heading{position:absolute;top:1059px;font-size:9.5px;font-weight:600;color:var(--text-dark)}
.footer-about{position:absolute;left:166px;top:1076px;width:150px;font-size:8px;line-height:14px;color:#888}
.social{position:absolute;left:362px;top:1082px;display:flex;gap:12px}
.social span{font-size:9px;font-weight:600;color:#555;display:flex;align-items:center;gap:4px}
.social span i{display:inline-block;width:7px;height:7px;border-radius:50%;background:#555}
.social span:first-child{color:var(--blue)}
.social span:first-child i{background:var(--blue)}
.footer-contact{position:absolute;left:605px;top:1058px;font-size:8.5px;color:var(--muted);line-height:14px}
.footer-contact .phone{color:var(--blue);font-size:11px;font-weight:600}
.footer-contact .row{display:flex;gap:9px}
.bottom-bar{position:absolute;left:0;top:1150px;width:835px;height:50px;background:var(--blue);color:var(--white);font-size:8px;display:flex;align-items:center;justify-content:space-between;padding:0 36px 0 38px}
.bottom-links{display:flex;gap:22px}
</style>
</head>
<body>

<header class="site-header">
  <div class="brand"><span class="b1">MARSH</span><span class="b2">DENTAL</span></div>
  <nav class="main-nav">
    <div class="nav-item active">
      <svg width="14" height="12" viewBox="0 0 14 12"><path d="M7 0 0 6h2v6h4V8h2v4h4V6h2z" fill="#fff"/></svg>Home</div>
    <div class="nav-item">
      <svg width="10" height="12" viewBox="0 0 10 12"><path d="M1 1c2-1.5 3 0 4 0s2-1.5 4 0c1 2 0 4-1 6l-1 4H6L5 8 4 11H3L2 7C1 5 0 3 1 1z" fill="#a9b3bd"/></svg>Services</div>
    <div class="nav-item">
      <svg width="16" height="12" viewBox="0 0 16 12"><path d="M1 2h14c0 6-3 9-7 9S1 8 1 2z" fill="#a9b3bd"/><rect x="4" y="3" width="8" height="2" fill="#fff"/></svg>Practice</div>
    <div class="nav-item">
      <svg width="12" height="14" viewBox="0 0 12 14"><rect x="1" y="1" width="10" height="13" fill="none" stroke="#a9b3bd" stroke-width="1.5"/><rect x="3.5" y="4" width="2" height="2" fill="#a9b3bd"/><rect x="6.5" y="4" width="2" height="2" fill="#a9b3bd"/><rect x="3.5" y="7.5" width="2" height="2" fill="#a9b3bd"/><rect x="6.5" y="7.5" width="2" height="2" fill="#a9b3bd"/></svg>Health Funds</div>
    <div class="nav-item">
      <svg width="12" height="13" viewBox="0 0 12 13"><circle cx="6" cy="3.5" r="3.2" fill="#a9b3bd"/><path d="M0 13c0-4 2.5-6 6-6s6 2 6 6z" fill="#a9b3bd"/></svg>About</div>
    <div class="nav-item">
      <svg width="15" height="11" viewBox="0 0 15 11"><rect width="15" height="11" rx="1" fill="#a9b3bd"/><path d="M0 1l7.5 5L15 1" stroke="#fff" stroke-width="1.3" fill="none"/></svg>Contact</div>
  </nav>
  <div class="header-contact">
    <div class="row"><svg width="9" height="12" viewBox="0 0 9 12"><path d="M2 0 4 3 2.5 4.5C3 6.5 4.5 8 6 9L7.5 8 9 10.5 7.5 12C3 10.5 0 6 0 1.5z" fill="#b5bcc3"/></svg><span class="phone">+1800 5 27140</span></div>
    <div class="row" style="margin-top:3px"><svg width="9" height="12" viewBox="0 0 9 12"><path d="M4.5 0A4.5 4.5 0 0 0 0 4.5C0 8 4.5 12 4.5 12S9 8 9 4.5A4.5 4.5 0 0 0 4.5 0z" fill="#b5bcc3"/><circle cx="4.5" cy="4.5" r="1.6" fill="#fff"/></svg><span>48 Carrow St.<br>Brenton Qld 4120</span></div>
  </div>
</header>

<section class="hero">
  <div class="hero-photo" role="img" aria-label="Photo of a smiling dentist holding a clipboard beside a happy family in a bright clinic"></div>
  <div class="hero-title">Your Local Family Friendly Dentist</div>
  <div class="hero-sub">Modern dental treatment can be<br>achieved with no or minimal discomfort</div>
  <div class="btn-solid hero-btn">Book Appointment</div>
</section>

<div class="info-card" style="left:36px">
  <h3>About Us</h3>
  <p>Lorem ipsum dolor sit amet, consecte tur adipiscing elit. Ut eu nisl quis augue suscipit dignissim.</p>
  <div class="btn-outline filled">Read More</div><div class="fold"></div>
</div>
<div class="info-card" style="left:227px">
  <h3>Health Funds</h3>
  <p>Etiam posuere tincidunt risus et elementum. Morbi condimentum, nunc non ornare dignissim.</p>
  <div class="btn-outline">Read More</div><div class="fold"></div>
</div>
<div class="info-card" style="left:418px">
  <h3>Practices</h3>
  <p>Quisque magna sapien, dapibus ac volutpat adipiscing, lacinia varius sapien aliquam facilisis.</p>
  <div class="btn-outline">Read More</div><div class="fold"></div>
</div>
<div class="info-card" style="left:609px;width:191px">
  <h3 style="margin-bottom:4px">Schedule</h3>
  <div class="schedule-row"><span>Monday - Friday</span><span>8:00 am - Late</span></div>
  <div class="schedule-row"><span>Saturday</span><span>8:00 am - 12:00 pm</span></div>
  <div class="schedule-row"><span>Sunday</span><span>Closed</span></div>
  <div class="fold"></div>
</div>

<h2 class="section-title" style="left:39px;top:508px;font-size:21px">Your Family Friendly Dentist</h2>
<div class="intro-photo" role="img" aria-label="Photo of a mother brushing her baby's teeth"></div>
<p class="intro-text">From the team of 1800 Smile Care, previously known as Dr. Owen Tallis's Dental Surgery, we would like to formally welcome you to our exciting new dental practice.</p>
<p class="intro-strong">We strive to provide you with a wide range of treatment options:</p>
<div class="treatments">
  <div class="treatment"><svg width="18" height="18" viewBox="0 0 18 18"><circle cx="9" cy="9" r="8" fill="none" stroke="#0a7fcf" stroke-width="1.2"/><path d="M5.5 5.5c1.5-1 2.5 0 3.5 0s2-1 3.5 0c.6 1.6 0 3-.8 4.5l-.7 3h-.8L9.5 11l-.8 2h-.8L7 10c-.8-1.5-1.4-2.9-1.5-4.5z" fill="#0a7fcf"/></svg>Dental check-up and oral health advice</div>
  <div class="treatment"><svg width="18" height="18" viewBox="0 0 18 18"><circle cx="9" cy="9" r="8" fill="none" stroke="#0a7fcf" stroke-width="1.2"/><path d="M5.5 5.5c1.5-1 2.5 0 3.5 0s2-1 3.5 0c.6 1.6 0 3-.8 4.5l-.7 3h-.8L9.5 11l-.8 2h-.8L7 10c-.8-1.5-1.4-2.9-1.5-4.5z" fill="#0a7fcf"/></svg>Paediatric (children's) dentistry</div>
  <div class="treatment"><svg width="18" height="18" viewBox="0 0 18 18"><circle cx="9" cy="9" r="8" fill="none" stroke="#0a7fcf" stroke-width="1.2"/><path d="M5.5 5.5c1.5-1 2.5 0 3.5 0s2-1 3.5 0c.6 1.6 0 3-.8 4.5l-.7 3h-.8L9.5 11l-.8 2h-.8L7 10c-.8-1.5-1.4-2.9-1.5-4.5z" fill="#0a7fcf"/></svg>Scaling and cleaning</div>
  <div class="treatment"><svg width="18" height="18" viewBox="0 0 18 18"><circle cx="9" cy="9" r="8" fill="none" stroke="#0a7fcf" stroke-width="1.2"/><path d="M5.5 5.5c1.5-1 2.5 0 3.5 0s2-1 3.5 0c.6 1.6 0 3-.8 4.5l-.7 3h-.8L9.5 11l-.8 2h-.8L7 10c-.8-1.5-1.4-2.9-1.5-4.5z" fill="#0a7fcf"/></svg>Teeth whitening</div>
  <div class="treatment"><svg width="18" height="18" viewBox="0 0 18 18"><circle cx="9" cy="9" r="8" fill="none" stroke="#0a7fcf" stroke-width="1.2"/><path d="M5.5 5.5c1.5-1 2.5 0 3.5 0s2-1 3.5 0c.6 1.6 0 3-.8 4.5l-.7 3h-.8L9.5 11l-.8 2h-.8L7 10c-.8-1.5-1.4-2.9-1.5-4.5z" fill="#0a7fcf"/></svg>Gum disease treatment</div>
  <div class="treatment"><svg width="18" height="18" viewBox="0 0 18 18"><circle cx="9" cy="9" r="8" fill="none" stroke="#0a7fcf" stroke-width="1.2"/><path d="M5.5 5.5c1.5-1 2.5 0 3.5 0s2-1 3.5 0c.6 1.6 0 3-.8 4.5l-.7 3h-.8L9.5 11l-.8 2h-.8L7 10c-.8-1.5-1.4-2.9-1.5-4.5z" fill="#0a7fcf"/></svg>Root canal treatment</div>
  <div class="treatment"><svg width="18" height="18" viewBox="0 0 18 18"><circle cx="9" cy="9" r="8" fill="none" stroke="#0a7fcf" stroke-width="1.2"/><path d="M5.5 5.5c1.5-1 2.5 0 3.5 0s2-1 3.5 0c.6 1.6 0 3-.8 4.5l-.7 3h-.8L9.5 11l-.8 2h-.8L7 10c-.8-1.5-1.4-2.9-1.5-4.5z" fill="#0a7fcf"/></svg>Dental fillings or restorations</div>
  <div class="treatment"><svg width="18" height="18" viewBox="0 0 18 18"><circle cx="9" cy="9" r="8" fill="none" stroke="#0a7fcf" stroke-width="1.2"/><path d="M5.5 5.5c1.5-1 2.5 0 3.5 0s2-1 3.5 0c.6 1.6 0 3-.8 4.5l-.7 3h-.8L9.5 11l-.8 2h-.8L7 10c-.8-1.5-1.4-2.9-1.5-4.5z" fill="#0a7fcf"/></svg>Tooth extraction (removal)</div>
  <div class="treatment"><svg width="18" height="18" viewBox="0 0 18 18"><circle cx="9" cy="9" r="8" fill="none" stroke="#0a7fcf" stroke-width="1.2"/><path d="M5.5 5.5c1.5-1 2.5 0 3.5 0s2-1 3.5 0c.6 1.6 0 3-.8 4.5l-.7 3h-.8L9.5 11l-.8 2h-.8L7 10c-.8-1.5-1.4-2.9-1.5-4.5z" fill="#0a7fcf"/></svg>Crowns and bridges</div>
  <div class="treatment"><svg width="18" height="18" viewBox="0 0 18 18"><circle cx="9" cy="9" r="8" fill="none" stroke="#0a7fcf" stroke-width="1.2"/><path d="M5.5 5.5c1.5-1 2.5 0 3.5 0s2-1 3.5 0c.6 1.6 0 3-.8 4.5l-.7 3h-.8L9.5 11l-.8 2h-.8L7 10c-.8-1.5-1.4-2.9-1.5-4.5z" fill="#0a7fcf"/></svg>Fitting of dentures</div>
  <div class="treatment"><svg width="18" height="18" viewBox="0 0 18 18"><circle cx="9" cy="9" r="8" fill="none" stroke="#0a7fcf" stroke-width="1.2"/><path d="M5.5 5.5c1.5-1 2.5 0 3.5 0s2-1 3.5 0c.6 1.6 0 3-.8 4.5l-.7 3h-.8L9.5 11l-.8 2h-.8L7 10c-.8-1.5-1.4-2.9-1.5-4.5z" fill="#0a7fcf"/></svg>Dental implants (artificial teeth)</div>
  <div class="treatment"><svg width="18" height="18" viewBox="0 0 18 18"><circle cx="9" cy="9" r="8" fill="none" stroke="#0a7fcf" stroke-width="1.2"/><path d="M5.5 5.5c1.5-1 2.5 0 3.5 0s2-1 3.5 0c.6 1.6 0 3-.8 4.5l-.7 3h-.8L9.5 11l-.8 2h-.8L7 10c-.8-1.5-1.4-2.9-1.5-4.5z" fill="#0a7fcf"/></svg>Fitting of mouthguards</div>
</div>

<aside class="booking">
  <div class="booking-head">
    <svg width="13" height="13" viewBox="0 0 13 13"><rect x=".7" y="2" width="11.6" height="10.3" fill="none" stroke="#fff" stroke-width="1.2"/><rect x="3" y="0" width="1.4" height="3" fill="#fff"/><rect x="8.6" y="0" width="1.4" height="3" fill="#fff"/><path d="M1 5h11M4.5 5v7M8.5 5v7M1 8.5h11" stroke="#fff" stroke-width=".8"/></svg>
    Book An Appointment<div class="fold"></div>
  </div>
  <div class="field" style="top:50px">Select Service<span class="caret"><svg width="7" height="4" viewBox="0 0 7 4"><path d="M0 0h7L3.5 4z" fill="#0a7fcf"/></svg></span></div>
  <div class="field" style="top:79px">First Name (required)</div>
  <div class="field" style="top:108px">Last Name</div>
  <div class="field" style="top:137px">Phone (required)</div>
  <div class="field typed" style="top:166px">jane.roe@mail|</div>
  <div class="field" style="top:195px">Date of Appointment (required)</div>
  <div class="btn-solid submit">Submit</div>
</aside>

<article class="member" style="left:35px">
  <div class="member-photo" role="img" aria-label="Portrait of team member Clara Whitby"></div>
  <h4>Clara Whitby</h4><p>Lorem ipsum dolor sit amet, teft consecte tur adipiscing elit ut eunt nisl quis augue.</p>
</article>
<article class="member" style="left:226px">
  <div class="member-photo" role="img" aria-label="Portrait of team member Neil Foster"></div>
  <h4>Neil Foster</h4><p>Lorem ipsum dolor sit amet, teft consecte tur adipiscing elit ut eunt nisl quis augue.</p>
</article>
<article class="member" style="left:417px">
  <div class="member-photo" role="img" aria-label="Portrait of team member Hannah Reyes"></div>
  <h4>Hannah Reyes</h4><p>Lorem ipsum dolor sit amet, teft consecte tur adipiscing elit ut eunt nisl quis augue.</p>
</article>

<h2 class="section-title" style="left:605px;top:800px;font-size:24px">Our Team</h2>
<p class="team-text">Lorem ipsum dolor sit amet, consectetur adipiscing elit. Ut volutpat rutrum eros sit amet sollicitudin. Suspendisse pulvinar, velit nec pharetra niba tefra.</p>
<div class="btn-solid team-btn">View All</div>
<div class="arrow-btn" style="left:610px;background:var(--blue)"><svg width="6" height="8" viewBox="0 0 6 8"><path d="M5 0 1 4l4 4" stroke="#fff" stroke-width="1.6" fill="none"/></svg></div>
<div class="arrow-btn" style="left:633px"><svg width="6" height="8" viewBox="0 0 6 8"><path d="M1 0l4 4-4 4" stroke="#0a7fcf" stroke-width="1.6" fill="none"/></svg></div>

<footer>
  <div class="footer-brand"><span class="b1">MARSH</span><span class="b2">DENTAL</span></div>
  <h5 class="footer-heading" style="left:166px">ABOUT US</h5>
  <p class="footer-about">Lorem ipsum dolor sit amet, teft consecte tur adipiscing elit ut eunt nisl quis augue.</p>
  <h5 class="footer-heading" style="left:362px">SOCIAL MEDIA</h5>
  <div class="social"><span><i></i>Circle</span><span><i></i>Chirp</span><span><i></i>Plus</span><span><i></i>Linkup</span><span><i></i>Feed</span></div>
  <div class="footer-contact">
    <div class="row"><svg width="9" height="12" viewBox="0 0 9 12"><path d="M2 0 4 3 2.5 4.5C3 6.5 4.5 8 6 9L7.5 8 9 10.5 7.5 12C3 10.5 0 6 0 1.5z" fill="#b5bcc3"/></svg><span class="phone">+1800 5 27140</span></div>
    <div class="row" style="margin-top:3px"><svg width="9" height="12" viewBox="0 0 9 12"><path d="M4.5 0A4.5 4.5 0 0 0 0 4.5C0 8 4.5 12 4.5 12S9 8 9 4.5A4.5 4.5 0 0 0 4.5 0z" fill="#b5bcc3"/><circle cx="4.5" cy="4.5" r="1.6" fill="#fff"/></svg><span>48 Carrow St.<br>Brenton Qld 4120</span></div>
  </div>
  <div class="bottom-bar">
    <span>Copyright 2014 Dental Site | All Rights Reserved | Privacy Policy &nbsp;| &nbsp;Site Map</span>
    <nav class="bottom-links"><span>Home</span><span>Services</span><span>Practice</span><span>Health Funds</span><span>About</span><span>Contact</span></nav>
  </div>
</footer>

</body>
</html>
```